Todo-list with focus on focus

We are writing todo app which is a to-do list/ outliner with focus support based on pomodoro method.

Attached are very rough mockups, but they are conceptually correct.

Main idea behind an app - minimum (unneeded) functionality and maximum benefit to the user.

So, everything must be very intuitive, fast, and without distractions (let's say Quince-style)

Target Market(s)

People who want to spend less time organizing their todo list than using it

Industry/Entity Type

It Support

Requirements
Must have
• Everything which is in mockups, maybe you can drop 1 or 2 if absolutely needed.
Nice to have
• 1. We would like to see such pallete here: http://www.huebinder.net/swatch/482716/Quiet_Harbor_Dusk but it's not mandatory.
If you propose some other pallete, please make sure it's beautiful.

2. It would be good to somehow indicate that project is a goal in project list, and task is a goal in goal's list

3. Inbox should be accessible easliy, probably by sticking it to the top of Projects list somehow.

4. If you are able to propose another way to deal with such amount of options to deal with tasks other than radial menu - you are free to do it, if it'll work.

5. Priority, tags - very nice to have if they will fit into conception.

6. Maybe you can add other stuff we have overlooked.
But, if added, it must be very simple and needed.

```html
<!DOCTYPE html>
<html lang="en">
<head>
<meta charset="utf-8">
<title>Focus Todo – Screens</title>
<link rel="stylesheet" href="https://fonts.googleapis.com/css2?family=Open+Sans:wght@400;600;700&display=swap">
<style>
  :root {
    --page-bg: #e9eaea;
    --screen-bg: #f1f1f1;
    --teal: #22a898;
    --teal-dark: #178a7c;
    --teal-light: #5cc4b6;
    --bar-top: #ffffff;
    --bar-bottom: #e4e4e4;
    --bar-text: #b3b3b3;
    --bar-text-strong: #a6a6a6;
    --active-row: #d2d2d2;
    --status-bg: #f7f7f7;
    --status-text: #5a5a5a;
    --toolbar-top: #f4f4f4;
    --toolbar-bottom: #d9d9d9;
    --icon: #7c7c7c;
    --muted: #9a9a9a;
  }
  * { box-sizing: border-box; margin: 0; padding: 0; }
  html, body { width: 1200px; height: 964px; overflow: hidden; }
  body {
    background: var(--page-bg);
    font-family: "Open Sans", Arial, sans-serif;
    position: relative;
  }
  .screen {
    position: absolute;
    top: 148px;
    width: 440px;
    height: 668px;
    background: var(--screen-bg);
    overflow: hidden;
    box-shadow: 0 2px 14px rgba(0,0,0,.12);
  }
  .screen--focus { left: 120px; }
  .screen--projects { left: 640px; }

  .status-bar {
    position: absolute; left: 0; top: 0; width: 100%; height: 27px;
    background: var(--status-bg);
    color: var(--status-text);
    font-size: 12px; font-weight: 600;
    display: flex; align-items: center; padding: 0 10px;
  }
  .status-bar .carrier { display: flex; align-items: center; gap: 5px; position: relative; z-index: 1; }
  .status-bar .clock { position: absolute; left: 0; right: 0; text-align: center; }
  .status-bar .battery { margin-left: auto; position: relative; z-index: 1; }

  .app-header {
    position: absolute; left: 0; top: 27px; width: 100%; height: 56px;
    background: linear-gradient(var(--teal-light), var(--teal) 45%, var(--teal-dark));
    color: #fff; font-weight: 700; font-size: 28px;
    display: flex; align-items: center; justify-content: center;
  }

  .bar {
    position: absolute;
    background: linear-gradient(var(--bar-top), var(--bar-bottom));
    border-radius: 4px;
    box-shadow: 0 2px 3px rgba(0,0,0,.12);
    color: var(--bar-text);
    font-weight: 600;
    display: flex; align-items: center;
    padding-left: 18px;
    white-space: nowrap;
  }
  .bar--active { background: var(--active-row); box-shadow: none; color: var(--bar-text-strong); }

  .focus-label { position: absolute; left: 14px; top: 88px; font-size: 17px; color: var(--muted); font-weight: 600; }
  .current-task { left: 18px; top: 117px; width: 342px; height: 45px; font-size: 30px; }
  .pomodoro-row {
    position: absolute; left: 22px; top: 190px; display: flex; gap: 2px;
  }
  .pomodoro-row .cell { width: 19px; height: 22px; display: flex; align-items: center; justify-content: center; }
  .pomodoro-row .cell--empty { background: linear-gradient(#fafafa, #e6e6e6); border: 1px solid #e0e0e0; }
  .timer { position: absolute; left: 20px; top: 222px; font-size: 86px; font-weight: 600; color: var(--teal); letter-spacing: -2px; line-height: 1; }
  .stop-button { left: 260px; top: 238px; width: 168px; height: 56px; font-size: 26px; justify-content: center; padding: 0; }
  .goal-group { font-size: 30px; left: 20px; width: 410px; height: 52px; }
  .goal-group--daily { top: 343px; }
  .goal-group--weekly { top: 501px; }
  .goal-group--life { top: 560px; height: 49px; }
  .goal-item { left: 58px; top: 406px; width: 372px; height: 50px; font-size: 25px; gap: 10px; }

  .toolbar {
    position: absolute; left: 0; bottom: 0; width: 100%; height: 48px;
    background: linear-gradient(var(--toolbar-top), var(--toolbar-bottom));
    border-top: 1px solid #cfcfcf;
    display: flex; align-items: center; justify-content: space-around; padding: 0 20px;
  }
  .toolbar .tool { width: 52px; height: 40px; display: flex; align-items: center; justify-content: center; }
  .toolbar .tool--active { background: #c4c4c4; box-shadow: inset 0 1px 3px rgba(0,0,0,.2); }

  .inbox-button {
    position: absolute; left: 18px; top: 92px; width: 97px; height: 64px;
    background: linear-gradient(#ffffff, #e8e8e8);
    border: 1px solid #d6d6d6;
    box-shadow: 0 2px 4px rgba(0,0,0,.15);
    display: flex; align-items: center; justify-content: center; gap: 4px;
    color: var(--teal); font-weight: 700; font-size: 16px;
  }
  .new-project {
    position: absolute; left: 167px; top: 115px; width: 185px; height: 27px;
    background: #fff; border: 1px solid #d8d8d8;
    font-size: 11px; color: #b0b0b0; display: flex; align-items: center; padding-left: 10px;
  }
  .add-project { position: absolute; left: 366px; top: 112px; font-size: 26px; font-weight: 700; color: #555; line-height: 1; }
  .project { font-size: 28px; }
  .subproject { font-size: 24px; }
  .subsubproject { font-size: 20px; }
</style>
</head>
<body>

<section class="screen screen--focus">
  <div class="status-bar">
    <span class="carrier">
      <svg width="18" height="10" viewBox="0 0 18 10"><rect x="0" y="7" width="3" height="3" fill="#5a5a5a"/><rect x="4" y="5" width="3" height="5" fill="#5a5a5a"/><rect x="8" y="3" width="3" height="7" fill="#5a5a5a"/><rect x="12" y="0" width="3" height="10" fill="#5a5a5a"/></svg>
      Orvilo
      <svg width="16" height="12" viewBox="0 0 16 12"><path d="M1 4a10 10 0 0 1 14 0M3.5 6.5a6.5 6.5 0 0 1 9 0M6 9a3 3 0 0 1 4 0" fill="none" stroke="#5a5a5a" stroke-width="1.6"/></svg>
    </span>
    <span class="clock">12:34 PM</span>
    <span class="battery"><svg width="26" height="12" viewBox="0 0 26 12"><rect x="0.5" y="0.5" width="22" height="11" rx="2" fill="none" stroke="#5a5a5a"/><rect x="2" y="2" width="19" height="8" fill="#5a5a5a"/><rect x="23" y="4" width="2.5" height="4" fill="#5a5a5a"/></svg></span>
  </div>
  <header class="app-header">App Name</header>

  <p class="focus-label">I'm noe focused on</p>
  <div class="bar current-task">Task Lorem Ipsum</div>

  <div class="pomodoro-row">
    <span class="cell"><svg width="14" height="12" viewBox="0 0 14 12"><path d="M1 6l4 4 8-9" fill="none" stroke="#22a898" stroke-width="2.4"/></svg></span>
    <span class="cell"><svg width="14" height="12" viewBox="0 0 14 12"><path d="M1 6l4 4 8-9" fill="none" stroke="#22a898" stroke-width="2.4"/></svg></span>
    <span class="cell"><svg width="14" height="12" viewBox="0 0 14 12"><path d="M1 6l4 4 8-9" fill="none" stroke="#22a898" stroke-width="2.4"/></svg></span>
    <span class="cell"><svg width="14" height="12" viewBox="0 0 14 12"><path d="M1 6l4 4 8-9" fill="none" stroke="#22a898" stroke-width="2.4"/></svg></span>
    <span class="cell"><svg width="14" height="12" viewBox="0 0 14 12"><path d="M1 6l4 4 8-9" fill="none" stroke="#22a898" stroke-width="2.4"/></svg></span>
    <span class="cell"><svg width="14" height="12" viewBox="0 0 14 12"><path d="M1 6l4 4 8-9" fill="none" stroke="#22a898" stroke-width="2.4"/></svg></span>
    <span class="cell"><svg width="14" height="12" viewBox="0 0 14 12"><path d="M1 6l4 4 8-9" fill="none" stroke="#22a898" stroke-width="2.4"/></svg></span>
    <span class="cell"><svg width="14" height="12" viewBox="0 0 14 12"><path d="M1 6l4 4 8-9" fill="none" stroke="#22a898" stroke-width="2.4"/></svg></span>
    <span class="cell"><svg width="14" height="12" viewBox="0 0 14 12"><path d="M1 6l4 4 8-9" fill="none" stroke="#22a898" stroke-width="2.4"/></svg></span>
    <span class="cell"><svg width="14" height="12" viewBox="0 0 14 12"><path d="M1 6l4 4 8-9" fill="none" stroke="#22a898" stroke-width="2.4"/></svg></span>
    <span class="cell cell--empty"></span>
    <span class="cell cell--empty"></span>
    <span class="cell cell--empty"></span>
    <span class="cell cell--empty"></span>
    <span class="cell cell--empty"></span>
    <span class="cell cell--empty"></span>
    <span class="cell cell--empty"></span>
    <span class="cell cell--empty"></span>
  </div>

  <div class="timer">21:34</div>
  <div class="bar stop-button">Stop</div>

  <div class="bar goal-group goal-group--daily">Daily Goals</div>
  <div class="bar goal-item">
    <svg width="22" height="20" viewBox="0 0 22 20"><path d="M2 10l6 7L20 2" fill="none" stroke="#22a898" stroke-width="3.2"/></svg>
    Goal Name
  </div>
  <div class="bar goal-group goal-group--weekly">Weekly Goals</div>
  <div class="bar goal-group goal-group--life">Life Goals</div>

  <nav class="toolbar">
    <span class="tool"><svg width="22" height="16" viewBox="0 0 22 16"><path d="M0 8l10-8v5h12v6H10v5z" fill="#7c7c7c"/></svg></span>
    <span class="tool"><svg width="22" height="16" viewBox="0 0 22 16"><path d="M22 8L12 0v5H0v6h12v5z" fill="#7c7c7c"/></svg></span>
    <span class="tool"><svg width="24" height="22" viewBox="0 0 24 22"><path d="M12 0L0 11h3v11h6v-7h6v7h6V11h3z" fill="#7c7c7c"/></svg></span>
    <span class="tool tool--active"><svg width="18" height="20" viewBox="0 0 18 20"><path d="M1 1v14l4-4 4 8 3-1.5-4-7.5h6z" fill="#6a6a6a"/></svg></span>
    <span class="tool"><svg width="22" height="22" viewBox="0 0 22 22"><g fill="#7c7c7c"><circle cx="11" cy="11" r="7"/><rect x="9" y="0" width="4" height="22"/><rect x="0" y="9" width="22" height="4"/><rect x="9" y="0" width="4" height="22" transform="rotate(45 11 11)"/><rect x="9" y="0" width="4" height="22" transform="rotate(-45 11 11)"/></g><circle cx="11" cy="11" r="3.2" fill="#e6e6e6"/></svg></span>
  </nav>
</section>

<section class="screen screen--projects">
  <div class="status-bar">
    <span class="carrier">
      <svg width="18" height="10" viewBox="0 0 18 10"><rect x="0" y="7" width="3" height="3" fill="#5a5a5a"/><rect x="4" y="5" width="3" height="5" fill="#5a5a5a"/><rect x="8" y="3" width="3" height="7" fill="#5a5a5a"/><rect x="12" y="0" width="3" height="10" fill="#5a5a5a"/></svg>
      Orvilo
      <svg width="16" height="12" viewBox="0 0 16 12"><path d="M1 4a10 10 0 0 1 14 0M3.5 6.5a6.5 6.5 0 0 1 9 0M6 9a3 3 0 0 1 4 0" fill="none" stroke="#5a5a5a" stroke-width="1.6"/></svg>
    </span>
    <span class="clock">12:34 PM</span>
    <span class="battery"><svg width="26" height="12" viewBox="0 0 26 12"><rect x="0.5" y="0.5" width="22" height="11" rx="2" fill="none" stroke="#5a5a5a"/><rect x="2" y="2" width="19" height="8" fill="#5a5a5a"/><rect x="23" y="4" width="2.5" height="4" fill="#5a5a5a"/></svg></span>
  </div>
  <header class="app-header">App Name</header>

  <div class="inbox-button">
    <svg width="40" height="40" viewBox="0 0 40 40"><rect x="1" y="1" width="38" height="38" fill="#22a898"/><path d="M20 6v17M13 16l7 7 7-7" fill="none" stroke="#fff" stroke-width="3.4"/><path d="M8 22v9h24v-9" fill="none" stroke="#fff" stroke-width="3.4"/></svg>
    Inbox
  </div>
  <div class="new-project">Type new project here</div>
  <div class="add-project">+</div>

  <div class="bar project" style="left:0;top:171px;width:428px;height:50px;padding-left:30px;">Project 01</div>
  <div class="bar subproject" style="left:59px;top:228px;width:367px;height:52px;padding-left:26px;">Subproject 01</div>
  <div class="bar subproject" style="left:59px;top:287px;width:367px;height:50px;padding-left:32px;">Subproject 02</div>
  <div class="bar subsubproject" style="left:117px;top:343px;width:309px;height:52px;padding-left:36px;">Subsubproject 01</div>
  <div class="bar bar--active project" style="left:11px;top:424px;width:417px;height:50px;padding-left:20px;">Project 02</div>
  <div class="bar subproject" style="left:63px;top:481px;width:365px;height:52px;padding-left:30px;">Subproject 01</div>
  <div class="bar project" style="left:0;top:553px;width:428px;height:52px;padding-left:30px;">Project 03</div>

  <nav class="toolbar">
    <span class="tool"><svg width="22" height="16" viewBox="0 0 22 16"><path d="M0 8l10-8v5h12v6H10v5z" fill="#7c7c7c"/></svg></span>
    <span class="tool"><svg width="22" height="16" viewBox="0 0 22 16"><path d="M22 8L12 0v5H0v6h12v5z" fill="#7c7c7c"/></svg></span>
    <span class="tool"><svg width="24" height="22" viewBox="0 0 24 22"><path d="M12 0L0 11h3v11h6v-7h6v7h6V11h3z" fill="#7c7c7c"/></svg></span>
    <span class="tool tool--active"><svg width="18" height="20" viewBox="0 0 18 20"><path d="M1 1v14l4-4 4 8 3-1.5-4-7.5h6z" fill="#6a6a6a"/></svg></span>
    <span class="tool"><svg width="22" height="22" viewBox="0 0 22 22"><g fill="#7c7c7c"><circle cx="11" cy="11" r="7"/><rect x="9" y="0" width="4" height="22"/><rect x="0" y="9" width="22" height="4"/><rect x="9" y="0" width="4" height="22" transform="rotate(45 11 11)"/><rect x="9" y="0" width="4" height="22" transform="rotate(-45 11 11)"/></g><circle cx="11" cy="11" r="3.2" fill="#e6e6e6"/></svg></span>
  </nav>
</section>

</body>
</html>
```